Looking for a cool & simple business-card-design for digital agency

Hi!

We are a web agency that offers Reputation Management, Zorvik & Seo Services and software development. We like cool things, we like innovative styles.

We have uploaded our logo.

Project Deadline Extended Reason: Client does not want any designs with the colorful logo. Please send us submissions ONLY with the blac and white logo. What the client would like to see:1) Back of the card: is a silver logo on a black background2) front of the card with all the data, please use white background and black logo thank you Added Friday, May 8, 2015

Software

```html
<!DOCTYPE html>
<html lang="de">
<head>
<meta charset="utf-8">
<title>Nordwerk AG – Visitenkarte</title>
<link rel="stylesheet" href="https://fonts.googleapis.com/css2?family=Lato:wght@400;700&display=swap">
<style>
  :root {
    --backdrop: #e9ece8;
    --card: #ffffff;
    --card-edge: #c9ccc9;
    --ink: #1f1f1f;
    --ink-soft: #2b2b2b;
  }
  html, body {
    margin: 0;
    padding: 0;
    width: 1200px;
    height: 969px;
    overflow: hidden;
    background: var(--backdrop);
    font-family: "Lato", Arial, sans-serif;
    color: var(--ink);
  }
  .business-card {
    position: absolute;
    left: 100px;
    top: 206px;
    width: 1000px;
    height: 556px;
    background: var(--card);
    border: 1px solid var(--card-edge);
    box-sizing: border-box;
  }
  .brand {
    position: absolute;
    left: 0;
    right: 0;
    top: 96px;
    display: flex;
    justify-content: center;
    align-items: center;
    gap: 18px;
  }
  .brand-square {
    width: 46px;
    height: 46px;
    background: var(--ink);
  }
  .brand-name {
    font-size: 54px;
    font-weight: 700;
    letter-spacing: 1px;
    line-height: 1;
    color: var(--ink);
  }
  .holder {
    position: absolute;
    left: 0;
    right: 0;
    top: 290px;
    display: flex;
    justify-content: center;
    align-items: center;
    gap: 22px;
  }
  .holder-name {
    font-size: 31px;
    font-weight: 700;
    color: var(--ink-soft);
  }
  .holder-divider {
    width: 3px;
    height: 52px;
    background: var(--ink);
  }
  .holder-role {
    font-size: 28px;
    font-weight: 400;
    color: var(--ink-soft);
  }
  .contact-row {
    position: absolute;
    left: 0;
    right: 0;
    top: 470px;
    display: flex;
    justify-content: center;
    align-items: center;
    gap: 24px;
    font-size: 25px;
    color: var(--ink-soft);
  }
  .contact-item {
    display: flex;
    align-items: center;
    gap: 9px;
  }
  .contact-icon {
    width: 26px;
    height: 26px;
    fill: var(--ink);
  }
</style>
</head>
<body>
  <div class="business-card">
    <div class="brand">
      <div class="brand-square"></div>
      <div class="brand-name">Nordwerk AG</div>
    </div>

    <div class="holder">
      <span class="holder-name">Lena Marsh</span>
      <span class="holder-divider"></span>
      <span class="holder-role">Director</span>
    </div>

    <div class="contact-row">
      <span class="contact-item">
        <svg class="contact-icon" viewBox="0 0 24 24" aria-hidden="true">
          <path d="M3 9c0-3 4-5 9-5s9 2 9 5v1.5h-4.5V8.5c-1.3-.6-2.8-.9-4.5-.9s-3.2.3-4.5.9v2H3z"/>
          <path d="M6.5 11.5h11l2.5 7.5H4z"/>
        </svg>
        000 555 0142
      </span>
      <span class="contact-item">
        <svg class="contact-icon" viewBox="0 0 24 24" aria-hidden="true">
          <path d="M2 5h20v14H2z M4 7v.4l8 6 8-6V7z M4 9.9V17h16V9.9l-8 6z" fill-rule="evenodd"/>
        </svg>
        info@nordwerkag.com
      </span>
      <span class="contact-item">
        <svg class="contact-icon" viewBox="0 0 24 24" aria-hidden="true">
          <path fill-rule="evenodd" d="M12 2a10 10 0 1 1 0 20a10 10 0 0 1 0-20z M4.1 11h3.4c.1-2.4.6-4.6 1.4-6.2A8 8 0 0 0 4.1 11z M9.5 11h5c-.2-3.3-1.3-6.4-2.5-7-1.2.6-2.3 3.7-2.5 7z M16.5 11h3.4a8 8 0 0 0-4.8-6.2c.8 1.6 1.3 3.8 1.4 6.2z M4.1 13a8 8 0 0 0 4.8 6.2c-.8-1.6-1.3-3.8-1.4-6.2z M9.5 13c.2 3.3 1.3 6.4 2.5 7 1.2-.6 2.3-3.7 2.5-7z M16.5 13c-.1 2.4-.6 4.6-1.4 6.2a8 8 0 0 0 4.8-6.2z"/>
        </svg>
        www.nordwerkag.com
      </span>
    </div>
  </div>
</body>
</html>
```